Medical Supply company in need of mail flyers

We are a medical supply company based out of West Palm Beach, Florida. Our website is StrideFreeBoots.Com but we also go by Velorin Medical Supply. We provide shoes through various insurance companies at no cost to the client.We're in need of multiple mail flyers for diabetic footwear customer retention. We will be choosing the top 2 designs submitted.

Industry/Entity Type

Medical Equipment

Requirements
Must have
• Flyers must be 6x9

```html
<!DOCTYPE html>
<html lang="en">
<head>
<meta charset="utf-8">
<title>Diabetic Footwear – Mail Flyer</title>
<link rel="stylesheet" href="https://fonts.googleapis.com/css2?family=Montserrat:wght@400;600;800;900&family=Arimo:wght@400;700&display=swap">
<style>
  :root {
    --green: #8dc67a;
    --green-deep: #6fb25c;
    --slate: #6e7f98;
    --slate-dark: #56667e;
    --navy: #3f5f8f;
    --ink: #1d1d1d;
    --paper: #ffffff;
    --photo-a: #55705e;
    --photo-b: #8a7a5c;
  }
  * { box-sizing: border-box; margin: 0; padding: 0; }
  html, body { width: 992px; height: 1200px; overflow: hidden; background: var(--paper); }
  .flyer {
    position: relative;
    width: 992px;
    height: 1200px;
    background: var(--paper);
    font-family: "Arimo", Arial, sans-serif;
    color: var(--ink);
    overflow: hidden;
  }
  .accent-bar {
    position: absolute; left: 0; top: 96px; width: 70px; height: 470px;
    background: var(--green);
  }
  .product-photo {
    position: absolute; left: 70px; top: 96px; width: 470px; height: 470px;
    background: linear-gradient(150deg, var(--photo-a) 0%, #7a8a68 40%, var(--photo-b) 75%, #6b6a5a 100%);
  }
  .photo-tint {
    position: absolute; left: 70px; top: 96px; width: 470px; height: 470px;
  }
  .title-panel {
    position: absolute; left: 540px; top: 96px; width: 420px; height: 520px;
    background: linear-gradient(160deg, var(--slate) 0%, var(--slate-dark) 100%);
  }
  .title {
    position: absolute; left: 572px; top: 470px; width: 370px;
    font-family: "Montserrat", sans-serif; font-weight: 900;
    font-size: 52px; line-height: 1.05; letter-spacing: 1px;
    color: var(--paper); text-transform: uppercase;
  }
  .steps-panel { position: absolute; left: 0; top: 566px; width: 600px; height: 364px; }
  .steps-number {
    position: absolute; left: 60px; top: 590px;
    font-family: "Montserrat", sans-serif; font-weight: 900;
    font-size: 210px; line-height: 1; color: var(--paper);
  }
  .steps-text {
    position: absolute; left: 225px; top: 635px;
    font-family: "Montserrat", sans-serif; font-weight: 600;
    font-size: 32px; line-height: 1.12; color: var(--paper); text-transform: uppercase;
  }
  .about { position: absolute; left: 600px; top: 650px; width: 350px; }
  .about-heading {
    font-family: "Montserrat", sans-serif; font-weight: 600;
    font-size: 26px; color: var(--navy); margin-bottom: 10px;
  }
  .about-heading .highlight { color: var(--green-deep); }
  .about-body { font-size: 16px; line-height: 1.32; }
  .rule { position: absolute; left: 60px; width: 880px; height: 4px; background: var(--slate); }
  .rule-top { top: 942px; }
  .rule-bottom { top: 1060px; }
  .contact-row {
    position: absolute; left: 60px; top: 978px; width: 880px;
    display: flex; justify-content: space-between; align-items: center;
  }
  .contact { display: flex; align-items: center; gap: 14px; font-size: 24px; }
  .contact svg { width: 36px; height: 36px; flex: none; }
  .brand-row {
    position: absolute; left: 60px; top: 1092px; width: 880px;
    display: flex; justify-content: space-between; align-items: center;
  }
  .brand {
    font-family: "Montserrat", sans-serif; font-weight: 600;
    font-size: 40px; color: var(--ink);
    display: flex; align-items: center; gap: 14px;
  }
  .brand-alt { color: var(--navy); }
  .brand-dot { width: 30px; height: 30px; border-radius: 50%; background: var(--green); }
</style>
</head>
<body>
<main class="flyer">
  <div class="accent-bar"></div>
  <div class="product-photo" role="img" aria-label="Photo of several leather therapeutic shoes arranged on a weathered wooden dock"></div>
  <svg class="photo-tint" viewBox="0 0 470 470" aria-hidden="true">
    <polygon points="0,0 260,0 0,260" fill="#8dc67a" opacity="0.35"/>
    <polygon points="470,470 210,470 470,210" fill="#8dc67a" opacity="0.3"/>
  </svg>

  <div class="title-panel"></div>
  <h1 class="title">Diabetic<br>Footwear</h1>

  <svg class="steps-panel" viewBox="0 0 600 364" aria-hidden="true">
    <polygon points="60,0 490,0 560,182 490,364 60,364" fill="var(--green)"/>
  </svg>
  <div class="steps-number">4</div>
  <p class="steps-text">Easy steps<br>to receive<br>your new<br>therapeutic<br>shoes.</p>

  <section class="about">
    <h2 class="about-heading">ABOUT <span class="highlight">US</span></h2>
    <p class="about-body">Stride Free Boots was created by Velorin Medical Supply to educate clients and prospective shoe fitters about diabetic shoes and the coverage that Medicare provides. Founded by a Board-Certified Pedorthist, the company's mission is to help clients receive properly fitted shoes from qualified healthcare professionals around the United States. Velorin Medical Supply works directly with Medicare to determine the patient's coverage.</p>
  </section>

  <div class="rule rule-top"></div>
  <div class="contact-row">
    <div class="contact">
      <svg viewBox="0 0 40 40" aria-hidden="true">
        <circle cx="20" cy="20" r="17" fill="none" stroke="var(--green)" stroke-width="3"/>
        <path d="M14 12c1-1 2.5-1 3 0l2 3c.5 1 0 2-1 2.5 1 2.5 2.5 4 5 5 .5-1 1.5-1.5 2.5-1l3 2c1 .5 1 2 0 3-3 3-9 0-12-3s-5.5-8.5-2.5-11.5z" fill="var(--green)"/>
      </svg>
      <span>1-800-555-0142</span>
    </div>
    <div class="contact">
      <svg viewBox="0 0 40 40" aria-hidden="true">
        <circle cx="20" cy="20" r="17" fill="none" stroke="var(--green)" stroke-width="3"/>
        <rect x="11" y="14" width="18" height="12" fill="none" stroke="var(--green)" stroke-width="2.5"/>
        <path d="M11 14l9 7 9-7" fill="none" stroke="var(--green)" stroke-width="2.5"/>
      </svg>
      <span>orders@stridefreeboots.com</span>
    </div>
  </div>
  <div class="rule rule-bottom"></div>

  <div class="brand-row">
    <div class="brand">Velorin Medical</div>
    <div class="brand brand-alt"><span class="brand-dot"></span>StrideFreeBoots</div>
  </div>
</main>
</body>
</html>
```